Redesign of the Klammbrot label

I am a pharmacist and sell a bitters called "Klammbrot". I would like to revise and modernize the current logo of my "Klammbrot". I have attached a photo of the current label. I have different bottle sizes with different label sizes, but for now I will only need one label for the 700ml size:
20ml 36x47mm
40ml 45x62mm
200ml 70x91mm
350ml 70x98mm
500ml 70x110mm
700ml 87x119mm
The Uffe is a small stream that runs through our town. The Klammbrot is a play on words that takes up the mysticism of the Harz, as a spirit can of course also be a schnapps. I like the mysticism and rough nature of the Harz in connection with the product. I have attached a logo suggestion that I once had an AI design. But I am very open to new ideas. A connection to my pharmacy does not necessarily have to be recognizable. VG, K. Brandis

Target Market(s)

End consumers, gastronomy, restaurants, hotels

```html
<!DOCTYPE html>
<html lang="de">
<head>
<meta charset="utf-8">
<title>Klammbrot – Etikett 700ml</title>
<link href="https://fonts.googleapis.com/css2?family=Alegreya+Sans:wght@800;900&family=Cutive&family=Fira+Sans+Extra+Condensed:wght@700&display=swap" rel="stylesheet">
<style>
  :root{
    --ink:#000;
    --paper:#fff;
    --stage:#fff;
    --crest-tone:#d9d9d9;
  }
  html,body{margin:0;padding:0;width:1200px;height:866px;overflow:hidden;background:var(--stage);}
  .canvas{position:relative;width:1200px;height:866px;}
  .label{
    position:absolute;left:326px;top:58px;width:548px;height:750px;
    background:var(--ink);border-radius:58px;color:var(--paper);
  }
  .label-frame{position:absolute;border:2.5px solid var(--paper);}
  .label-frame--outer{inset:13px;border-radius:46px;}
  .label-frame--inner{inset:21px;border-radius:38px;}
  .centered{position:absolute;left:0;right:0;text-align:center;}
  .brand-title{
    top:46px;font-family:"Alegreya Sans",sans-serif;font-weight:900;
    font-size:48px;letter-spacing:1.5px;line-height:1;
  }
  .quality-banner{position:absolute;left:354px;top:99px;width:126px;height:48px;}
  .quality-banner span{
    position:absolute;left:0;right:0;top:2px;text-align:center;color:var(--ink);
    font-family:"Fira Sans Extra Condensed",sans-serif;font-weight:700;font-size:21px;letter-spacing:.5px;
  }
  .crest-placeholder{
    position:absolute;left:213px;top:102px;width:120px;height:122px;
    background:var(--crest-tone);border-radius:50% 50% 46% 46%;
  }
  .product-name{position:absolute;left:150px;top:218px;width:248px;height:50px;}
  .product-name text{
    font-family:"Alegreya Sans",sans-serif;font-weight:900;font-size:30px;fill:var(--paper);letter-spacing:2px;
  }
  .product-type{
    top:264px;font-family:"Alegreya Sans",sans-serif;font-weight:800;font-size:20px;
    letter-spacing:1.2px;line-height:25px;
  }
  .product-story{
    top:349px;font-family:"Cutive",serif;font-size:16.5px;line-height:24.5px;
  }
  .pharmacy{position:absolute;left:53px;top:552px;width:208px;height:78px;}
  .pharmacy-mark{
    position:absolute;left:0;top:2px;width:68px;height:68px;border:2.5px solid var(--paper);border-radius:50%;
  }
  .pharmacy-text{
    position:absolute;left:76px;top:0;width:138px;text-align:center;
    font-family:"Alegreya Sans",sans-serif;font-weight:900;font-size:17px;line-height:20px;letter-spacing:.6px;
  }
  .pharmacy-text .intro{font-family:"Cutive",serif;font-weight:400;font-size:15.5px;letter-spacing:0;}
  .address{
    position:absolute;left:285px;top:543px;width:228px;text-align:center;
    font-family:"Alegreya Sans",sans-serif;font-weight:900;font-size:17.5px;line-height:20px;letter-spacing:.6px;
  }
  .volume{top:664px;font-family:"Cutive",serif;font-size:19px;}
  .lot{top:696px;font-family:"Cutive",serif;font-size:14.5px;}
</style>
</head>
<body>
<div class="canvas">
  <section class="label">
    <div class="label-frame label-frame--outer"></div>
    <div class="label-frame label-frame--inner"></div>

    <div class="centered brand-title">TALBACHER</div>

    <div class="quality-banner">
      <svg width="126" height="48" viewBox="0 0 126 48">
        <polygon points="0,0 126,0 126,48 63,34 0,48" fill="#fff"/>
      </svg>
      <span>ERLESENER</span>
    </div>

    <div class="crest-placeholder" role="img" aria-label="Wappenadler mit Krone, weiß auf schwarz"></div>

    <svg class="product-name" viewBox="0 0 248 50">
      <defs><path id="arch" d="M4,46 Q124,22 244,46"/></defs>
      <text text-anchor="middle"><textPath href="#arch" startOffset="50%">KLAMMBROT</textPath></text>
    </svg>

    <div class="centered product-type">Bitterlikör<br>nach alter Apothekerkunst</div>

    <div class="centered product-story">
      Eine Zubereitung nach höchst geheimem<br>
      Rezept. Sie sei empfohlen zum Genuss nach<br>
      einem guten Mahl.<br>
      Aufs Feinste zubereitet mit geistigen Auszügen<br>
      von Enzian. Kalmus. Malabar-Kardamom und<br>
      anderen wertvollen Zutaten.
    </div>

    <div class="pharmacy">
      <div class="pharmacy-mark"></div>
      <div class="pharmacy-text">
        <span class="intro">Aus der</span><br>ST. LORENZ<br>APOTHEKE<br>TALBACH
      </div>
    </div>

    <div class="address">
      DR. K. BRANDIS<br>MÜHLENGASSE 12<br>37999 TALBACH,<br>TEL. 05599-4181
    </div>

    <div class="centered volume">700ml 34% vol</div>
    <div class="centered lot">kräuterlikör chininhaltig L2313886</div>
  </section>
</div>
</body>
</html>
```